Business Card for Toffee Parlour

I have a logo for my candy buffet business, and need a business card designed using that logo. Toffee Parlour designs and builds beautiful and delicious candy and dessert tables for all kinds of events. The card should be simple, modern, graphic, colorful, and use the Toffee Parlour Logo.

Target Market(s)

The target market is people hosting major parties and events. This includes brides getting married, parents hosting birthday parties/Sweet Sixteen/Bar Mitzvah/quinceanera parties, and companies hosting corporate events.

Industry/Entity Type

Business

Requirements
Must have
• The business card must have the logo, with or without the tag line.

The following information must be on the card:

Renata Hollis
CEO & Candy Stylist
415.372.6091
renata@toffeeparlourco.example
Nice to have
• I like the idea of having multiple colors of the same design so that several people receiving cards will each receive a different color. Perhaps 3-5 colors or variations on a basic card design.

```html
<!DOCTYPE html>
<html lang="en">
<head>
<meta charset="utf-8">
<title>Toffee Parlour — Business Cards</title>
<link rel="stylesheet" href="https://fonts.googleapis.com/css2?family=Montserrat:wght@700&family=Quicksand:wght@300;400;500&display=swap">
<style>
  :root {
    --page: #f1f0ec;
    --ink: #1c1c1c;
    --paper: #ffffff;
    --sky: #1ebdf0;
    --sky-art: #8fd8f4;
    --berry: #f5067c;
    --berry-art: #fb9cc8;
    --grape: #6a4ba1;
    --grape-art: #b7a3da;
    --dot: #f5067c;
  }
  * { box-sizing: border-box; margin: 0; padding: 0; }
  html, body {
    width: 1200px; height: 1000px; overflow: hidden;
    background: var(--page);
  }
  .card-sheet {
    position: relative;
    width: 1200px; height: 1000px;
    display: grid;
    grid-template-columns: 500px 500px;
    grid-template-rows: 286px 286px;
    gap: 60px;
    justify-content: center;
    align-content: center;
  }
  .card {
    position: relative;
    width: 500px; height: 286px;
    overflow: hidden;
    box-shadow: 0 6px 18px rgba(0,0,0,.12);
  }
  /* Front */
  .card--front {
    background: var(--paper);
    display: flex; align-items: center; justify-content: center;
  }
  .brand {
    display: flex; align-items: center; gap: 16px;
  }
  .brand__dot {
    width: 34px; height: 34px; border-radius: 50%;
    background: var(--dot);
  }
  .brand__name {
    font-family: "Quicksand", sans-serif;
    font-weight: 500;
    font-size: 52px;
    letter-spacing: 1px;
    color: var(--ink);
    line-height: 1;
  }
  /* Backs */
  .card--back { color: #fff; padding: 30px 34px; }
  .card--sky { background: var(--sky); }
  .card--berry { background: var(--berry); }
  .card--grape { background: var(--grape); }
  .contact__name {
    font-family: "Montserrat", sans-serif;
    font-weight: 700;
    font-size: 30px;
    letter-spacing: 1px;
    line-height: 1.1;
  }
  .contact__title {
    font-family: "Quicksand", sans-serif;
    font-weight: 400;
    font-size: 17px;
    letter-spacing: 1px;
    margin-top: 2px;
  }
  .contact__phone {
    font-family: "Quicksand", sans-serif;
    font-weight: 300;
    font-size: 36px;
    letter-spacing: 4px;
    margin-top: 34px;
    line-height: 1;
  }
  .contact__email {
    font-family: "Quicksand", sans-serif;
    font-weight: 400;
    font-size: 15px;
    letter-spacing: 1px;
    margin-top: 8px;
  }
  .candy-art {
    position: absolute;
    right: 0; bottom: 0;
    width: 210px; height: 160px;
    border-top-left-radius: 90px;
  }
  .card--sky .candy-art { background: linear-gradient(135deg, var(--sky-art), rgba(255,255,255,.55)); }
  .card--berry .candy-art { background: linear-gradient(135deg, var(--berry-art), rgba(255,255,255,.55)); }
  .card--grape .candy-art { background: linear-gradient(135deg, var(--grape-art), rgba(255,255,255,.55)); }
</style>
</head>
<body>
  <main class="card-sheet">
    <section class="card card--front">
      <div class="brand">
        <span class="brand__dot"></span>
        <span class="brand__name">Toffee Parlour</span>
      </div>
    </section>

    <section class="card card--back card--sky">
      <p class="contact__name">Renata Hollis</p>
      <p class="contact__title">CEO &amp; Candy Stylist</p>
      <p class="contact__phone">415.372.6091</p>
      <p class="contact__email">renata@toffeeparlourco.example</p>
      <div class="candy-art" role="img" aria-label="Illustration of swirl lollipops, a candy cane and wrapped sweets"></div>
    </section>

    <section class="card card--back card--berry">
      <p class="contact__name">Renata Hollis</p>
      <p class="contact__title">CEO &amp; Candy Stylist</p>
      <p class="contact__phone">415.372.6091</p>
      <p class="contact__email">renata@toffeeparlourco.example</p>
      <div class="candy-art" role="img" aria-label="Illustration of swirl lollipops, a candy cane and wrapped sweets"></div>
    </section>

    <section class="card card--back card--grape">
      <p class="contact__name">Renata Hollis</p>
      <p class="contact__title">CEO &amp; Candy Stylist</p>
      <p class="contact__phone">415.372.6091</p>
      <p class="contact__email">renata@toffeeparlourco.example</p>
      <div class="candy-art" role="img" aria-label="Illustration of swirl lollipops, a candy cane and wrapped sweets"></div>
    </section>
  </main>
</body>
</html>
```